HTML one page email

I need a ready-to-email, HTML email designed. It should be relatively simple. I am advertising my new children's book. The book is a 22 page children's book that is great for parents to read to kids and to give as a gift.

I would like the backround of the email to have the same colors as the book cover and a column on the right side of the email that is titled, "Newsworthy". Under that section, we'll have quotes from people about the book.

Target Market(s)

doctors, nurses, hospitals, libraries, bookfares

Industry/Entity Type

Advertising

Requirements
Must have
• Image of the front page, modern graphics, bright colors.

Links to the book's website - www.pebblehopgarden.com

Link to the book's site on Quillora.com - http://qlra.com/5127734920
Nice to have
• Incorporate some of the details of the press release into the copy.

```html
<!DOCTYPE html>
<html lang="en">
<head>
<meta charset="utf-8">
<title>Children's Book Announcement</title>
<link rel="stylesheet" href="https://fonts.googleapis.com/css2?family=Arimo:ital,wght@0,400;0,700;1,400&family=Fredoka:wght@600&display=swap">
<style>
  :root {
    --sky: #2ea9df;
    --paper: #ffffff;
    --frame-green: #3f8a4a;
    --header-orange: #fdb240;
    --body-lime: #c0da5f;
    --ink: #383838;
    --ink-soft: #444444;
    --accent-blue: #2ea9df;
    --link-blue: #0b5a9c;
    --rule-green: #3f8a4a;
    --cover-blue: #0ea2d9;
    --cover-green: #7cc646;
    --cover-orange: #fbad3c;
  }
  * { box-sizing: border-box; margin: 0; padding: 0; }
  html, body { width: 998px; height: 1200px; overflow: hidden; }
  body {
    background: var(--sky);
    font-family: "Arimo", Arial, sans-serif;
    color: var(--ink);
    position: relative;
  }
  .email-sheet {
    position: absolute;
    left: 87px; top: 27px;
    width: 821px; height: 1150px;
    background: var(--paper);
  }
  .email-frame {
    position: absolute;
    left: 17px; top: 23px;
    width: 787px; height: 1131px;
    border: 5px solid var(--frame-green);
    background: var(--body-lime);
    overflow: hidden;
  }
  .hero {
    height: 284px;
    background: var(--header-orange);
    text-align: center;
    padding-top: 48px;
  }
  .hero-title {
    font-weight: 400;
    font-size: 25px;
    line-height: 32px;
    color: var(--ink);
    width: 720px;
    margin: 0 auto;
  }
  .hero-rule {
    width: 707px;
    height: 1px;
    background: #fff3d8;
    margin: 25px auto 20px;
    border: 0;
  }
  .hero-subtitle {
    font-size: 20px;
    line-height: 24px;
    color: var(--ink);
  }
  .hero-subtitle strong { font-weight: 700; }

  .newsworthy {
    position: absolute;
    left: 38px; top: 329px;
    width: 302px; height: 705px;
    background: var(--paper);
    border-radius: 8px;
    padding: 22px 23px 0;
  }
  .newsworthy-title {
    text-align: center;
    font-weight: 700;
    font-size: 21px;
    color: var(--accent-blue);
    letter-spacing: 0.3px;
    padding-bottom: 14px;
    border-bottom: 1px solid var(--rule-green);
    margin-bottom: 16px;
  }
  .quote {
    font-style: italic;
    font-size: 13.6px;
    line-height: 18px;
    color: var(--ink-soft);
    margin-bottom: 10px;
  }
  .quote-source {
    font-weight: 700;
    font-size: 13.6px;
    color: var(--ink-soft);
    margin-bottom: 17px;
  }

  .book {
    position: absolute;
    left: 386px; top: 334px;
    width: 346px; height: 525px;
    background: var(--cover-blue);
    box-shadow: 1px 2px 5px rgba(0,0,0,0.45);
    border: 1px solid #6a7b52;
    padding: 22px 15px 22px 18px;
  }
  .book-art {
    width: 100%; height: 100%;
    background: linear-gradient(150deg, var(--cover-green) 0%, #a9d86d 35%, var(--cover-green) 62%, var(--cover-orange) 63%, var(--cover-orange) 100%);
  }
  .site-link {
    position: absolute;
    left: 0; width: 100%;
    padding-left: 377px;
    padding-right: 0;
    top: 906px;
    text-align: center;
    font-weight: 700;
    font-size: 17px;
    color: var(--link-blue);
    text-decoration: underline;
    width: 964px;
    left: -189px;
  }
  .buy-button {
    position: absolute;
    left: 455px; top: 969px;
    width: 209px; height: 46px;
    border-radius: 23px;
    background: var(--accent-blue);
    border: 3px solid var(--paper);
    color: var(--paper);
    font-family: "Fredoka", "Arial Rounded MT Bold", sans-serif;
    font-weight: 600;
    font-size: 19px;
    letter-spacing: 0.6px;
    text-align: center;
    line-height: 40px;
    text-decoration: none;
  }
</style>
</head>
<body>
  <div class="email-sheet">
    <div class="email-frame">
      <header class="hero">
        <h1 class="hero-title">Phoenix Otolaryngologist Harlan Brisbane Unveils Delightful New Children’s Book Reminding Children to Avoid Placing Things in Their Ears and Noses</h1>
        <hr class="hero-rule">
        <p class="hero-subtitle"><strong>“Don't Poke Pebbles Up Your Nose! Don't Drop Beads In Your Ears!”</strong><br>Focuses on Child Safety</p>
      </header>

      <aside class="newsworthy">
        <h2 class="newsworthy-title">NEWSWORTHY</h2>
        <p class="quote">Lorem ipsum dolor sit amet, consectetur adipiscing elit. Aenean ornare ultricies placerat. Cras ultrices ligula in orci varius sit amet malesuada dui tincidunt. Nam cursus venenatis sem a scelerisque.</p>
        <p class="quote-source">– Aenean Non Magna</p>
        <p class="quote">Aliquam metus odio, posuere non commodo vel, pellentesque nec lorem. Sed diam mi, porttitor vitae interdum in, molestie vitae massa. Sed accumsan libero neque, vel porta tortor.</p>
        <p class="quote-source">– Morbi Pellentesque</p>
        <p class="quote">Sed id leo augue, nec vestibulum urna. Donec volutpat faucibus luctus. Donec ac sem tellus. Ut nisi odio, bibendum eget varius id, consectetur eu magna.</p>
        <p class="quote-source">– Fusce Sollicitudin Posuere</p>
        <p class="quote">Sed aliquet facilisis lectus et pharetra. Fusce elementum hendrerit tellus, at dapibus augue placerat sit amet. Cum sociis natoque penatibus et magnis dis parturient montes, nascetur ridiculus mus.</p>
        <p class="quote-source">– Suspendisse Potenti</p>
      </aside>

      <div class="book">
        <div class="book-art" role="img" aria-label="Front cover of the children's book: cartoon nose with big ears and eyes, a frog and a stick, with the title and authors' names"></div>
      </div>

      <a class="site-link" href="http://www.pebblehopgarden.com">www.pebblehopgarden.com</a>
      <a class="buy-button" href="http://qlra.com/5127734920">BUY THE BOOK</a>
    </div>
  </div>
</body>
</html>
```